Refresh of Business Card Design

Want to refresh the business card design with the new logo while adhering to style guide as attached. Would like to match feel of website www.durmackvinex.com

```html
<!DOCTYPE html>
<html lang="en">
<head>
<meta charset="utf-8">
<title>Durmack Vinex — Business Card</title>
<link rel="stylesheet" href="https://fonts.googleapis.com/css2?family=Montserrat:wght@800&family=Work+Sans:wght@400;500&display=swap">
<style>
  :root {
    --stage: #3a3c40;
    --card-navy: #141b2c;
    --card-deep: #0b0f19;
    --accent-red: #e8274b;
    --text-white: #f2f3f5;
    --silver-dark: #6d7079;
    --silver-light: #f4f5f7;
    --sky-violet: #3a2f55;
    --sky-ember: #8a2f3a;
  }
  * { box-sizing: border-box; margin: 0; padding: 0; }
  html, body { width: 1200px; height: 900px; overflow: hidden; }
  body {
    background: var(--stage);
    font-family: "Work Sans", sans-serif;
    position: relative;
  }
  .card {
    position: absolute;
    width: 630px;
    height: 360px;
    border-radius: 26px;
    background: var(--card-navy);
    overflow: hidden;
  }
  .card--back { left: 60px; top: 50px; }
  .card--front {
    left: 510px; top: 490px;
    background: linear-gradient(135deg, var(--card-navy) 45%, var(--card-deep) 100%);
  }
  .scene-photo {
    position: absolute;
    left: 200px; top: 0;
    width: 430px; height: 220px;
    background:
      radial-gradient(ellipse at 45% 75%, rgba(138,47,58,.85) 0%, rgba(58,47,85,.55) 35%, rgba(20,27,44,0) 70%);
  }
  .silver-bar {
    position: absolute;
    left: 0; right: 0;
    top: 284px; height: 16px;
    background: linear-gradient(180deg, var(--silver-dark) 0%, var(--silver-light) 45%, #c9cbd0 60%, var(--silver-dark) 100%);
  }
  .site-url {
    position: absolute;
    left: 34px; top: 318px;
    color: var(--accent-red);
    font-size: 20px;
    letter-spacing: 5px;
  }
  .brand {
    position: absolute;
    right: 26px; top: 250px;
    display: flex; align-items: center; gap: 10px;
    background: var(--card-deep);
    border-radius: 30px;
    padding: 10px 18px 10px 10px;
  }
  .brand__dot {
    width: 30px; height: 30px;
    border-radius: 50%;
    background: var(--accent-red);
  }
  .brand__name {
    color: var(--text-white);
    font-size: 20px;
    font-weight: 500;
    letter-spacing: 1px;
  }
  .person {
    position: absolute;
    left: 46px; top: 112px;
  }
  .person__name {
    font-family: "Montserrat", sans-serif;
    font-weight: 800;
    font-size: 32px;
    color: var(--accent-red);
    letter-spacing: .5px;
  }
  .person__role {
    color: var(--text-white);
    font-size: 19px;
    margin-left: 30px;
    margin-top: 2px;
  }
  .contact-list {
    position: absolute;
    left: 62px; top: 184px;
    list-style: none;
    color: var(--text-white);
    font-size: 15.5px;
    line-height: 22px;
  }
  .contact-list li { display: flex; align-items: center; gap: 12px; }
  .contact-list svg { width: 14px; height: 14px; fill: var(--accent-red); flex: none; }
  .contact-list .no-icon { padding-left: 26px; }
</style>
</head>
<body>

<section class="card card--back" aria-label="Card back">
  <div class="silver-bar"></div>
  <div class="brand"><span class="brand__dot"></span><span class="brand__name">DURMACK VINEX</span></div>
  <p class="site-url">DurmackVinex.com</p>
</section>

<section class="card card--front" aria-label="Card front">
  <div class="scene-photo" role="img" aria-label="Oil field pumpjacks silhouetted against a sunset sky"></div>
  <div class="person">
    <h1 class="person__name">CORIN HALVEY</h1>
    <p class="person__role">Sales</p>
  </div>
  <ul class="contact-list">
    <li>
      <svg viewBox="0 0 24 24" aria-hidden="true"><path d="M6.6 10.8a15.2 15.2 0 0 0 6.6 6.6l2.2-2.2c.3-.3.7-.4 1-.2 1.1.4 2.3.6 3.6.6.6 0 1 .4 1 1V20c0 .6-.4 1-1 1A17 17 0 0 1 3 4c0-.6.4-1 1-1h3.5c.6 0 1 .4 1 1 0 1.3.2 2.5.6 3.6.1.3 0 .7-.2 1z"/></svg>
      555.014.2287
    </li>
    <li>
      <svg viewBox="0 0 24 24" aria-hidden="true"><path d="M2 5h20v14H2zm2 2v.4l8 5 8-5V7zm0 2.8V17h16V9.8l-8 5z"/></svg>
      Chalvey@durmackvinex.com
    </li>
    <li>
      <svg viewBox="0 0 24 24" aria-hidden="true"><path d="M12 2a7 7 0 0 0-7 7c0 5.2 7 13 7 13s7-7.8 7-13a7 7 0 0 0-7-7zm0 9.5A2.5 2.5 0 1 1 12 6.5a2.5 2.5 0 0 1 0 5z"/></svg>
      P.O.Box 40218 Larkfield, TX 79580
    </li>
    <li class="no-icon">72 Quarry Ln. Fenwick, Texas 79402</li>
  </ul>
  <div class="silver-bar"></div>
  <div class="brand"><span class="brand__dot"></span><span class="brand__name">DURMACK VINEX</span></div>
  <p class="site-url">DurmackVinex.com</p>
</section>

</body>
</html>
```